Web Design Project Bright Lantern

I am needing a website for a theatre called Bright Lantern Stage School (blstage.com) which has already been purchsed from web nest. (Let me know if you need any other info on that.)We need a website that is professional looking and easy to access. Attached is the logo as well as the business card design. I think it would be nice to have the same type of design that’s on the business card but I am definitely open to other creative ideas. I need the website to be in a format where I can edit it in the future when I need to add classes and events to it. Also, some other things I need are I need are a…
A homepage. On the homepage we would like the motto, “Rise to the spotlight.” Also, the mission statement,
Bright Lantern Stage School strives to help students achieve excellence in performance, while building self-confidence and creativity. The Bright Lantern Stage School has created a fun and safe environment, where students can learn, acquire new skills, and explore their potential through musical theatre. Students not only have the freedom to, but are encouraged to embrace who they are and can lose their fear of judgment from others.
Class Registration Page for the classes- (As well as a coin link option for each if that is possible)
4-6 Musical Theatre
Tuesday’s 4:00PM-5:00PM
January 6th – February 24th
8 Weeks
Cost $160
Curriculum: Moss Harbor
Class info: In MT 4-6 your students will learn the basics of singing, dancing, and acting. A lesson of theatre terminology or technique will be taught each week as well as working on the show that will be performed at the end of the 8 weeks semester.

6-9 Musical Theatre
Tuesday’s 5:15PM-6:45PM
January 6th- February 24th
8 Weeks
Cost: $200
Curriculum: Tilly
Class info: In MT 6-9 your students will learn the basics of singing, dancing, and acting. A lesson of theatre terminology or technique will be taught each week as well as working on the show that will be performed at the end of the 8 weeks semester.
9-12 Musical Theatre
Wednesday’s 5:00-7:00PM
8 Weeks
Cost: $240
Curriculum: Gilded
Class info: In MT 9-12 your students will learn intermediate levels of singing, dancing, and acting. A lesson of theatre terminology or technique will be taught each week as well as working on the show that will be performed at the end of the 8 weeks semester.

About- (Include headshot that is attached)
A native Coloradan, Maren is an actress, director, teacher, and wife. She was a Dean’s List graduate of Northridge College in Florida, she holds a B.S. degree in Theatre. Her Capstone Project involved writing, producing, directing, and starring in a 60-minute one-woman musical which was noted by the Chairman of Theatre as setting new standard for the NRC project. Initially attending Harmon College, Maren was one of nine students representing HC at the Great Plains Drama Festival. Maren has also been a senior theatre director at the Maplewood Youth Playhouse for 4 years, where she directed fall, spring, and summer classes for ages 4-19. Her experience includes directing the main stage production, Quill Jr., assistant director for, Keep Your Chin Up Milo Barnes, and stage management for Der Nachtvogel.

Contact us
Phone: 303-555-0147
Email: blstageschool.com

Also, I do not have any photos of students yet so it's ok if their aren't many pictures because I intend on adding some when things get going, so if it's simple that's great. Also, if you find any musical theatre pictures that don't include faces, are just bodies or feet, that would work as well.
Updates

The web address needs to be blstage.com. I have already purchased the domain name from WebNest. Let me know if there are any steps I might be missing or any other info I need to provide. Also, I need to be able to edit the website in the future but I'm not sure which format is best for that.

Target Market(s)

Theatre parents and students

Industry/Entity Type

Building

Requirements
Must have
• Stated above.

```html
<!DOCTYPE html>
<html lang="en">
<head>
<meta charset="utf-8">
<title>Bright Lantern Stage School</title>
<link rel="stylesheet" href="https://fonts.googleapis.com/css2?family=Ubuntu:wght@300;400;500&family=Roboto:wght@400&family=Oswald:wght@700&display=swap">
<style>
  :root{
    --red:#8b0000;
    --dark:#2a2a2a;
    --darker:#222222;
    --footer:#333333;
    --white:#ffffff;
    --text:#555555;
    --heading:#444444;
    --icon:#555555;
    --social:#1f6fa8;
  }
  *{margin:0;padding:0;box-sizing:border-box}
  html,body{width:1200px;height:1135px;overflow:hidden;background:var(--white)}
  body{position:relative;font-family:"Ubuntu",sans-serif;color:var(--text)}
  .abs{position:absolute}

  .brand{left:184px;top:40px;color:var(--red);font-family:"Ubuntu",sans-serif;font-weight:400;line-height:1.1}
  .brand-mark{position:absolute;left:0;top:6px;width:26px;height:26px;background:var(--red)}
  .brand-name{padding-left:36px;font-size:34px;display:block}
  .brand-sub{padding-left:36px;font-size:13px;letter-spacing:5px;display:block;text-transform:uppercase;margin-top:6px}

  .social-top{left:765px;top:57px;display:flex;gap:5px}
  .social-top span{width:26px;height:26px;border-radius:50%;background:var(--social)}

  .quick-top{right:171px;top:44px;text-align:right}
  .quick-top .label{font-size:16px;color:#222}
  .quick-top .phone{font-size:21px;color:var(--red);margin-top:6px}

  .hero{left:0;top:169px;width:1200px;height:645px;
    background:radial-gradient(ellipse at 58% 35%,#fbf1df 0%,#e9d3b3 35%,#b08a65 65%,#5a3b2a 100%)}
  .nav{left:171px;top:138px;width:858px;height:51px;background:var(--dark);display:flex;align-items:center;
    box-shadow:0 8px 18px rgba(0,0,0,.35)}
  .nav a{color:var(--white);text-decoration:none;font-size:13.5px;text-transform:uppercase;height:100%;
    display:flex;align-items:center;border-right:1px solid #3a3a3a}
  .nav a:last-child{border-right:none}

  .class-card{left:172px;top:420px;width:269px;height:394px}
  .card-title{height:120px;background:var(--red);color:var(--white);font-size:16px;text-align:center;padding-top:93px;text-transform:uppercase}
  .card-schedule{height:86px;background:var(--dark);color:var(--white);text-align:center;font-size:15px;line-height:21.5px;padding-top:11px}
  .card-info{height:188px;background:var(--red);color:var(--white);padding:14px 17px 0 19px}
  .card-info h3{font-weight:400;font-size:15.5px;margin-bottom:14px}
  .card-info p{font-size:10.8px;line-height:20.6px}
  .avatar{left:236px;top:357px;width:144px;height:144px;border-radius:50%;background:#9a9a9a;border:3px solid var(--white);
    box-shadow:0 4px 10px rgba(0,0,0,.4)}

  .motto{left:667px;top:385px;font-family:"Oswald",sans-serif;font-weight:700;font-style:italic;color:var(--red);
    font-size:62px;line-height:82px;text-transform:uppercase;letter-spacing:-2px}
  .arrow{top:568px;width:34px;height:34px;border-radius:50%;background:#555}
  .arrow svg{display:block}

  .class-tab{top:762px;width:269px;height:52px;background:var(--red);color:var(--white);font-size:15.5px;
    display:flex;align-items:center;justify-content:center;text-transform:uppercase}

  .welcome{left:171px;top:835px;width:858px;text-align:center}
  .welcome h1{font-family:"Roboto",sans-serif;font-weight:400;font-size:33px;color:var(--heading)}
  .welcome p{font-size:11.4px;line-height:20.5px;margin-top:12px;color:#666}

  .footer{left:0;top:981px;width:1200px;height:95px;background:var(--footer)}
  .footer-bottom{left:0;top:1076px;width:1200px;height:59px;background:var(--darker);color:var(--white);
    font-size:11px;text-align:center;line-height:59px}
  .foot-contact{left:171px;top:1000px;color:var(--white)}
  .foot-contact h2{font-weight:400;font-size:17.5px}
  .foot-contact p{font-size:14px;color:#bbb;margin-top:8px}
  .foot-address{left:549px;top:1000px;font-size:16px;line-height:27px;color:#ddd}
  .foot-social{left:836px;top:1011px;display:flex;gap:5px}
  .foot-social span{width:35px;height:35px;border-radius:50%;background:var(--icon)}
</style>
</head>
<body>
  <div class="abs brand">
    <span class="brand-mark"></span>
    <span class="brand-name">Bright Lantern</span>
    <span class="brand-sub">Stage School</span>
  </div>

  <div class="abs social-top" aria-label="Social links"><span></span><span></span><span></span></div>

  <div class="abs quick-top">
    <div class="label">Quick Contact</div>
    <div class="phone">303-555-0147</div>
  </div>

  <div class="abs hero" role="img" aria-label="Stage photo: cream theatre curtains above a crowd with raised hands"></div>

  <nav class="abs nav">
    <a href="#" style="padding:0 26px 0 31px">Home</a>
    <a href="#" style="padding:0 26px 0 26px">About Us</a>
    <a href="#" style="padding:0 26px 0 21px">Theatre Academy</a>
    <a href="#" style="padding:0 16px 0 23px">Our Locations</a>
    <a href="#" style="padding:0 21px 0 16px">Media Gallery</a>
    <a href="#" style="padding:0 20px 0 22px">Contact Us</a>
  </nav>

  <section class="abs class-card">
    <div class="card-title">4-6 Musical Theatre</div>
    <div class="card-schedule">
      Tuesday’s 4:00PM-5:00PM<br>January 6th – February 24th<br>8 Weeks&nbsp; Cost $160
    </div>
    <div class="card-info">
      <h3>Curriculum : Moss Harbor</h3>
      <p>Class info : &nbsp;In MT 4-6 your students will learn the basics of singing, dancing, and acting. A lesson of theatre terminology or technique will be taught each week as well as working on the show that will be performed at the end of the 8 weeks semester.</p>
    </div>
  </section>
  <div class="abs avatar" role="img" aria-label="Instructor headshot"></div>

  <div class="abs motto">Rise to<br>the spotlight</div>
  <div class="abs arrow" style="left:668px">
    <svg width="34" height="34" viewBox="0 0 34 34"><path d="M19 10l-7 7 7 7" fill="none" stroke="#fff" stroke-width="2.5"/></svg>
  </div>
  <div class="abs arrow" style="left:711px">
    <svg width="34" height="34" viewBox="0 0 34 34"><path d="M15 10l7 7-7 7" fill="none" stroke="#fff" stroke-width="2.5"/></svg>
  </div>

  <div class="abs class-tab" style="left:465px">6-9 Musical Theatre</div>
  <div class="abs class-tab" style="left:760px">9-12 Musical Theatre</div>

  <section class="abs welcome">
    <h1>Welcome To Bright Lantern</h1>
    <p>Bright Lantern Stage School strives to help students achieve excellence in performance, while building self-confidence and creativity. The Bright Lantern Stage School has created a fun and safe environment, where students can learn, acquire new skills, and explore their potential through musical theatre. Students not only have the freedom to, but are encouraged to embrace who they are and can lose their fear of judgment from others.</p>
  </section>

  <footer>
    <div class="abs footer"></div>
    <div class="abs foot-contact">
      <h2>Quick contact</h2>
      <p>Phone : +1 303-555-0147 &nbsp;/ info@blstage.com</p>
    </div>
    <div class="abs foot-address">4120 Lantern Way,<br>Denver, CO 80203.</div>
    <div class="abs foot-social" aria-label="Social links"><span></span><span></span><span></span><span></span><span></span></div>
    <div class="abs footer-bottom">© 2014 Bright Lantern - All Rights Reserved</div>
  </footer>
</body>
</html>
```